Vetern Mailer for Mortgage Refinance

Hello, I need some options in my KM mailers we send out here in the USA! A sample of our mailer has been included. I need all the verbiage the same. The data merge points need to stay on too. Please make this pop. We have a high end TAVU printer and a Z auto folding machine. Letter goes into a number 10 envelope with windows. So lets see what you can do. One with colors below is our company colors and then one black, white, gray.
Blue - 3399FF------ R 51 G 153 B 255
Orange - FF9933----- R 255 G 153 B 51
Black – 333333------ R 51 G 51 B 51
White – FFFFFF------ R 255 G 255 B 255

Target Market(s)

United States Military Service Members

Industry/Entity Type

Mortgage Lender

Requirements
Must have
• Margins for folding with Z and Number 10 Envelope with two windows

```html
<!DOCTYPE html>
<html lang="en">
<head>
<meta charset="utf-8">
<title>KM Refinance Mailer</title>
<link rel="stylesheet" href="https://fonts.googleapis.com/css2?family=Poppins:wght@300;400;500;600;700;800&family=Rajdhani:wght@600;700&display=swap">
<style>
:root{
  --blue:#3399ff;
  --orange:#ff9933;
  --orange-deep:#e8892a;
  --ink:#333333;
  --white:#ffffff;
  --paper:#f3f3f3;
  --band:#dcdcdc;
  --peach:#fbe3c8;
  --field:#e4dfdf;
  --backdrop:#8b949d;
}
*{box-sizing:border-box;margin:0;padding:0}
html,body{width:1200px;height:2380px;overflow:hidden}
body{background:var(--backdrop);font-family:"Poppins",sans-serif;color:var(--ink);position:relative}
.page{position:absolute;left:150px;width:900px;height:1165px;background:var(--white);box-shadow:0 6px 24px rgba(0,0,0,.25);overflow:hidden}
.page-front{top:16px}
.page-back{top:1198px}
.abs{position:absolute}

/* address block */
.address-zone{left:0;top:0;width:900px;height:380px;background:var(--paper)}
.re-line{left:47px;top:44px;font-size:14px;font-weight:600;display:flex;align-items:center;gap:8px}
.loan-line{left:47px;top:74px;font-size:14px;display:flex;align-items:center;gap:8px}
.merge-bar{display:inline-block;height:16px;background:var(--blue);border-radius:2px}
.notice{left:47px;top:142px;width:460px;font-size:12px;line-height:1.35}
.recipient-name{left:47px;top:212px;font-size:20px;font-weight:700;letter-spacing:.2px}
.recipient-street{left:47px;top:240px;font-size:11.5px;line-height:1.3;display:flex;gap:6px}
.recipient-street span{width:180px}
.field{left:47px;width:190px;height:22px;background:var(--field);font-size:10.5px;padding:4px 8px;border-radius:1px}

/* offer panel */
.offer-card{left:572px;top:43px;width:278px;height:148px;background:var(--peach);border-radius:10px}
.offer-tag{left:590px;width:242px;height:26px;background:var(--orange);color:var(--white);border-radius:5px;font-size:13px;text-align:center;line-height:26px}
.offer-amount{left:572px;top:124px;width:278px;text-align:center;font-size:58px;font-weight:800;line-height:58px}
.offer-note{left:572px;top:210px;width:278px;text-align:center;font-size:13px;line-height:1.35}
.call-title{left:572px;top:262px;width:278px;text-align:center;font-family:"Rajdhani",sans-serif;font-weight:700;font-size:26px;color:var(--blue)}
.call-number{left:572px;top:294px;width:278px;text-align:center;font-size:20px;font-weight:700;display:flex;justify-content:center;align-items:center;gap:6px}
.hours{left:575px;top:321px;width:272px;height:30px;border:1.5px solid var(--blue);border-radius:4px;text-align:center;font-size:13px;line-height:27px}

/* letter */
.letter-box{left:47px;top:419px;width:808px;height:330px;border:1.5px solid var(--blue);background:#f6f6f6}
.letter-photo{left:60px;top:432px;width:323px;height:302px;border-radius:4px;border:2px solid #9cc8f0;background:linear-gradient(135deg,#b7c9d8 0%,#8aa2b8 45%,#5d534d 100%)}
.letter-text{left:405px;top:450px;width:435px;font-size:12.5px;line-height:1.45}
.letter-text h2{font-size:16px;font-weight:700;margin-bottom:8px}
.letter-text .check-back{font-size:17px;font-weight:700;line-height:1.3;margin-top:8px}

/* benefits band */
.benefit-band{left:0;top:780px;width:900px;height:385px;background:var(--band)}
.benefit-title{font-size:17px;font-weight:700}
.benefit-title.orange{color:var(--orange)}
.benefit-title.blue{color:var(--blue)}
.benefit-list{list-style:none;font-size:13px;line-height:1.65}
.benefit-list li{display:flex;align-items:center;gap:7px}
.col-divider{left:450px;top:812px;width:1px;height:120px;background:#a9a9a9}
.urgent-box{left:47px;top:944px;width:367px;height:96px;background:var(--orange-deep);color:#fde6cf;font-size:11px;line-height:1.4;padding:10px 12px}
.brand-block{left:497px;top:952px;display:flex;align-items:center;gap:12px}
.brand-dot{width:22px;height:22px;border-radius:50%;background:var(--blue)}
.brand-name{font-size:22px;font-weight:300;color:var(--blue);letter-spacing:1px;line-height:1.1}
.contact-row{left:497px;font-size:13px;display:flex;align-items:center;gap:10px}
.contact-row .merge-bar{width:255px}
.cashout{left:47px;top:1060px;display:flex;border:1.5px solid var(--blue);font-size:12px;font-weight:600;height:24px;line-height:21px}
.cashout .label{background:var(--blue);color:var(--white);padding:0 8px}
.cashout .value{color:var(--blue);padding:0 8px;background:var(--white)}
.footer-line{left:47px;top:1105px;display:flex;align-items:center;gap:14px;font-size:11.5px}
.nmls{display:flex;border:1.5px solid var(--blue);height:22px;line-height:19px;font-weight:700}
.nmls .label{background:var(--blue);color:var(--white);padding:0 6px}
.nmls .value{padding:0 8px;background:var(--white)}
.footer-company{font-weight:700}
.footer-address{display:flex;align-items:center;gap:4px}
.footer-note{font-size:8.5px;font-style:italic}

/* disclaimer page */
.disclaimer{left:45px;top:418px;width:810px;font-size:9.5px;line-height:1.4}
.disclaimer p{margin-bottom:6px}
.disclaimer .lead{font-weight:700}
.disclaimer h3{font-size:9.5px;font-weight:700;margin-top:8px}
.disclaimer h3.orange{color:var(--orange)}
.disclaimer h3.blue{color:var(--blue)}
</style>
</head>
<body>

<section class="page page-front">
  <div class="abs address-zone"></div>
  <div class="abs re-line">RE: <span class="merge-bar" style="width:245px"></span></div>
  <div class="abs loan-line">Loan ID Number <span class="merge-bar" style="width:160px"></span></div>
  <p class="abs notice">Summit Crest Home Loans LLC Is not affiliated with your current lender nor is it an agency of the Federal Government.</p>
  <div class="abs recipient-name">DANIEL CARTER</div>
  <div class="abs recipient-street">
    <svg width="12" height="14" viewBox="0 0 12 14"><path d="M6 0a5 5 0 0 0-5 5c0 3.5 5 9 5 9s5-5.5 5-9a5 5 0 0 0-5-5z" fill="var(--orange)"/><circle cx="6" cy="5" r="2" fill="#fff"/></svg>
    <span>Lorem ipsum dolor sit amet, consectetur</span>
  </div>
  <div class="abs field" style="top:280px">CITY:</div>
  <div class="abs field" style="top:308px">STATE:</div>
  <div class="abs field" style="top:336px">ZIP:</div>

  <div class="abs offer-card"></div>
  <div class="abs offer-tag" style="top:58px">Close_month</div>
  <div class="abs offer-tag" style="top:90px">Skip_month</div>
  <div class="abs offer-amount">$0</div>
  <p class="abs offer-note">You may be able to defer<br>your next two payments.<sup>1</sup></p>
  <div class="abs call-title">Call Toll Free</div>
  <div class="abs call-number">
    <svg width="17" height="17" viewBox="0 0 20 20"><circle cx="10" cy="10" r="10" fill="var(--orange)"/><path d="M7 5l2 2.5-1.2 1.3a7 7 0 0 0 3.4 3.4l1.3-1.2L15 13l-1.2 1.8c-4.5-.4-8.2-4.1-8.6-8.6z" fill="#fff"/></svg>
    0555 014 287
  </div>
  <div class="abs hours">Weekdays 6 a.m. to 5 p.m. PST</div>

  <div class="abs letter-box"></div>
  <div class="abs letter-photo" role="img" aria-label="Photo of a small model house and keys on a desk while a person signs mortgage papers"></div>
  <div class="abs letter-text">
    <h2>Dear Daniel,</h2>
    <p>We are contacting you regarding your &lt;&lt;balance&gt;&gt; KM loan. Our review has indicated that because of homes appreciating in &lt;&lt;city&gt;&gt;, you may now qualify for additional benefits. These benefits may include lowering your monthly mortgage payment, deferring up to two payments, refund of escrow, and $35,000 or more cash-out.<sup>3</sup> Call our KM Program Specialist at 0555 014 287 at your earliest convenience to receive a detailed explanation of how you may be able to access these benefits.<sup>4</sup></p>
    <p class="check-back">You may also receive a check back from your escrow account.<sup>2</sup></p>
  </div>

  <div class="abs benefit-band"></div>
  <div class="abs" style="left:47px;top:806px">
    <div class="benefit-title orange">Additional Benefits Include:</div>
    <ul class="benefit-list">
      <li><svg width="11" height="11" viewBox="0 0 12 12"><circle cx="6" cy="6" r="6" fill="var(--orange)"/><path d="M3.2 6.2l1.9 1.9 3.7-3.9" stroke="#fff" stroke-width="1.5" fill="none"/></svg>100% LTV Cash-Out Available</li>
      <li><svg width="11" height="11" viewBox="0 0 12 12"><circle cx="6" cy="6" r="6" fill="var(--orange)"/><path d="M3.2 6.2l1.9 1.9 3.7-3.9" stroke="#fff" stroke-width="1.5" fill="none"/></svg>Pay off High Interest Debt</li>
      <li><svg width="11" height="11" viewBox="0 0 12 12"><circle cx="6" cy="6" r="6" fill="var(--orange)"/><path d="M3.2 6.2l1.9 1.9 3.7-3.9" stroke="#fff" stroke-width="1.5" fill="none"/></svg>Complete a long overdue home renovation</li>
      <li><svg width="11" height="11" viewBox="0 0 12 12"><circle cx="6" cy="6" r="6" fill="var(--orange)"/><path d="M3.2 6.2l1.9 1.9 3.7-3.9" stroke="#fff" stroke-width="1.5" fill="none"/></svg>No out-of-pocket appraisal deposit</li>
      <li><svg width="11" height="11" viewBox="0 0 12 12"><circle cx="6" cy="6" r="6" fill="var(--orange)"/><path d="M3.2 6.2l1.9 1.9 3.7-3.9" stroke="#fff" stroke-width="1.5" fill="none"/></svg>No Private Mortgage Insurance</li>
    </ul>
  </div>
  <div class="abs col-divider"></div>
  <div class="abs" style="left:497px;top:806px">
    <div class="benefit-title blue">KM IRRRL Benefits</div>
    <ul class="benefit-list">
      <li><svg width="11" height="11" viewBox="0 0 12 12"><circle cx="6" cy="6" r="6" fill="var(--orange)"/><path d="M3.2 6.2l1.9 1.9 3.7-3.9" stroke="#fff" stroke-width="1.5" fill="none"/></svg>Reduce Your Current Interest Rate</li>
      <li><svg width="11" height="11" viewBox="0 0 12 12"><circle cx="6" cy="6" r="6" fill="var(--orange)"/><path d="M3.2 6.2l1.9 1.9 3.7-3.9" stroke="#fff" stroke-width="1.5" fill="none"/></svg>Mortgage-Only Credit Report</li>
      <li><svg width="11" height="11" viewBox="0 0 12 12"><circle cx="6" cy="6" r="6" fill="var(--orange)"/><path d="M3.2 6.2l1.9 1.9 3.7-3.9" stroke="#fff" stroke-width="1.5" fill="none"/></svg>No Appraisal Required</li>
      <li><svg width="11" height="11" viewBox="0 0 12 12"><circle cx="6" cy="6" r="6" fill="var(--orange)"/><path d="M3.2 6.2l1.9 1.9 3.7-3.9" stroke="#fff" stroke-width="1.5" fill="none"/></svg>Fast Closings in 8-14 days</li>
      <li><svg width="11" height="11" viewBox="0 0 12 12"><circle cx="6" cy="6" r="6" fill="var(--orange)"/><path d="M3.2 6.2l1.9 1.9 3.7-3.9" stroke="#fff" stroke-width="1.5" fill="none"/></svg>No Income or Asset Verification Required</li>
    </ul>
  </div>

  <div class="abs urgent-box">We recommend you call our office at &lt;&lt;phone_number&gt;&gt; within the next 3-5 business days as market rates fluctuate. By taking action now your next mortgage payment may not be due until &lt;&lt;next_pay_month&gt;&gt;.2 To avoid further delay, please call today.</div>

  <div class="abs brand-block">
    <span class="brand-dot"></span>
    <span class="brand-name">SUMMIT CREST<br>HOME LOANS</span>
  </div>
  <div class="abs contact-row" style="top:1040px">Phone Number <span class="merge-bar"></span></div>
  <div class="abs contact-row" style="top:1066px">Loan ID Number <span class="merge-bar" style="width:248px"></span></div>

  <div class="abs cashout"><span class="label">CASH OUT OPTIONS (TAX FREE)</span><span class="value">$35,000 OR MORE</span></div>

  <div class="abs footer-line">
    <span class="nmls"><span class="label">NMLS</span><span class="value">1000001</span></span>
    <span class="footer-company">Summit Crest Home Loans LLC</span>
    <span class="footer-address">
      <svg width="10" height="12" viewBox="0 0 12 14"><path d="M6 0a5 5 0 0 0-5 5c0 3.5 5 9 5 9s5-5.5 5-9a5 5 0 0 0-5-5z" fill="var(--orange)"/><circle cx="6" cy="5" r="2" fill="#fff"/></svg>
      4800 N Harbor Ridge Rd Ste 210 Mesa, AZ 85201
    </span>
    <span class="footer-note">*Please see reverse for disclaimer</span>
  </div>
</section>

<section class="page page-back">
  <div class="abs disclaimer">
    <p class="lead">Offer is available only for loans made or arranged through Summit Crest Home Loans LLC, NMLS 1000001, a private lender that is not associated with any government agency or your current servicer. Verification of employment may apply. This program is exclusive to the named recipient.</p>
    <h3 class="orange">TERMS AND CONDITIONS:</h3>
    <p>This offer is extended because you appear to meet certain criteria selected from information in a prescreened report from a consumer reporting agency. Final terms depend on your credit history, property value, income and available equity. If you no longer qualify when you apply, the offer may be withdrawn. You may opt out of future prescreened offers by contacting the major credit bureaus.</p>
    <h3 class="blue">State Disclosure Requirements:</h3>
    <p>Summit Crest Home Loans LLC is a licensed mortgage lender in the states where it does business. Licensing details for each state are available on request and through the national consumer access registry. Some states require additional disclosures, which will be provided with your application.</p>
    <h3>1. Deferred mortgage payments:</h3>
    <p>If you do not make your mortgage payment for the month that you are closing your new loan, it may be possible to add that amount to your new loan balance. Deferred interest increases the total you repay over the life of the loan. Late fees may still apply under your current loan terms.</p>
    <h3>2. Escrow Account Refund (if applicable):</h3>
    <p>If you have an escrow account with your mortgage, any refund is governed by the terms of your current lender. The timing and amount of a refund depend on the balance at the time of payoff. Please contact your current lender for details about your escrow account.</p>
    <h3>3. Example cash-out of $35,000</h3>
    <p>A cash-out amount is in addition to your monthly mortgage payment and assumes adequate equity in your property. A full appraisal may be required. Your actual rate and payment may differ. Please call one of our licensed loan officers for a personalized quote.</p>
    <h3>4. Your circumstances may vary</h3>
    <p>Please contact us to see how we may assist. Summit Crest Home Loans is an Equal Housing Lender. We do not discriminate on the basis of race, color, religion, national origin, sex, marital status, age or because income derives from any public assistance program.</p>
  </div>
</section>

</body>
</html>
```